Bref créative
Brant & Co. LLC
Commercial Real Estate/ Invesment Group/Commercial Investment Group
Simple
Thomas Verhoeven
Aquisitions/Development
Not needed
555-318-2096 not on stationary
tom@brantandcollc.example
brantandcollc.example

```html
<!DOCTYPE html>
<html lang="en">
<head>
<meta charset="utf-8">
<title>Brant &amp; Co. LLC – Business Cards</title>
<link rel="stylesheet" href="https://fonts.googleapis.com/css2?family=Arimo:wght@400;700&display=swap">
<style>
  :root {
    --backdrop: #e4e4e4;
    --card-white: #ffffff;
    --card-black: #050505;
    --ink-dark: #111111;
    --ink-grey: #6e6e6e;
    --ink-light: #f2f2f2;
    --silver-light: #f4f4f4;
    --silver-mid: #c2c2c2;
    --silver-dark: #8c8c8c;
    --logo-grey: #9a9a9a;
  }
  * { box-sizing: border-box; margin: 0; padding: 0; }
  html, body {
    width: 1200px; height: 804px; overflow: hidden;
    background: var(--backdrop);
    font-family: "Arimo", Arial, sans-serif;
  }
  .sheet { position: relative; width: 1200px; height: 804px; }
  .card {
    position: absolute; width: 555px; height: 270px;
    border-radius: 12px; overflow: hidden;
    box-shadow: 0 2px 6px rgba(0,0,0,.18);
  }
  .card--white { background: var(--card-white); color: var(--ink-dark); }
  .card--black { background: var(--card-black); color: var(--ink-light); }
  .card--front-white { left: 42px; top: 108px; }
  .card--front-black { left: 614px; top: 108px; }
  .card--back-white { left: 42px; top: 403px; }
  .card--back-black { left: 614px; top: 403px; }

  .swoosh { position: absolute; left: 0; top: 0; width: 100%; height: 100%; }

  .brand {
    position: absolute; display: flex; align-items: center; gap: 8px;
    font-size: 25px; font-weight: 400; letter-spacing: .5px; white-space: nowrap;
  }
  .brand__mark { width: 14px; height: 14px; background: currentColor; }
  .card--white .brand { color: var(--logo-grey); }
  .card--black .brand { color: var(--ink-light); }
  .brand--front { left: 24px; top: 88px; }
  .brand--back { left: 50%; top: 98px; transform: translateX(-50%); }

  .contact { position: absolute; left: 270px; top: 36px; }
  .contact__name { font-size: 17px; font-weight: 700; }
  .contact__role { font-size: 12px; color: var(--ink-grey); margin-top: 2px; }
  .card--black .contact__role { color: #bdbdbd; }
  .contact__list {
    margin-top: 22px; display: grid; grid-template-columns: 70px auto;
    column-gap: 6px; row-gap: 3px; font-size: 13px;
  }
  .contact__label { font-weight: 700; text-align: right; }
  .contact__value { color: var(--ink-grey); }
  .card--black .contact__value { color: #cfcfcf; }

  .web-line {
    position: absolute; left: 0; right: 0; bottom: 36px;
    text-align: center; font-size: 15px; letter-spacing: 1.5px;
  }
</style>
</head>
<body>
<main class="sheet">

  <section class="card card--white card--front-white">
    <svg class="swoosh" viewBox="0 0 555 270" preserveAspectRatio="none" aria-hidden="true">
      <defs>
        <linearGradient id="silver-on-white" x1="0" y1="0" x2="1" y2="1">
          <stop offset="0" stop-color="#e9e9e9"/>
          <stop offset=".5" stop-color="#b4b4b4"/>
          <stop offset="1" stop-color="#d8d8d8"/>
        </linearGradient>
      </defs>
      <path d="M0 196 C140 278 360 262 555 168 L555 270 L0 270 Z" fill="url(#silver-on-white)"/>
      <path d="M150 270 C320 258 450 222 555 176" fill="none" stroke="#111" stroke-width="3"/>
    </svg>
    <div class="brand brand--front"><span class="brand__mark"></span>Brant &amp; Co. LLC</div>
    <div class="contact">
      <p class="contact__name">Thomas Verhoeven</p>
      <p class="contact__role">Aquisitions/Development</p>
      <div class="contact__list">
        <span class="contact__label">Phone</span><span class="contact__value">555-204-7731</span>
        <span class="contact__label">Cell</span><span class="contact__value">555-318-2096</span>
        <span class="contact__label">Fax</span><span class="contact__value">555-907-4418</span>
        <span class="contact__label">Email</span><span class="contact__value">tom@brantandcollc.example</span>
        <span class="contact__label">Web</span><span class="contact__value">brantandcollc.example</span>
      </div>
    </div>
  </section>

  <section class="card card--black card--front-black">
    <svg class="swoosh" viewBox="0 0 555 270" preserveAspectRatio="none" aria-hidden="true">
      <defs>
        <linearGradient id="silver-on-black" x1="0" y1="0" x2="1" y2="1">
          <stop offset="0" stop-color="#f4f4f4"/>
          <stop offset=".5" stop-color="#bdbdbd"/>
          <stop offset="1" stop-color="#e6e6e6"/>
        </linearGradient>
      </defs>
      <path d="M0 196 C140 278 360 262 555 168 L555 270 L0 270 Z" fill="url(#silver-on-black)"/>
      <path d="M150 270 C320 258 450 222 555 176" fill="none" stroke="#050505" stroke-width="3"/>
    </svg>
    <div class="brand brand--front"><span class="brand__mark"></span>Brant &amp; Co. LLC</div>
    <div class="contact">
      <p class="contact__name">Thomas Verhoeven</p>
      <p class="contact__role">Aquisitions/Development</p>
      <div class="contact__list">
        <span class="contact__label">Phone</span><span class="contact__value">555-204-7731</span>
        <span class="contact__label">Cell</span><span class="contact__value">555-318-2096</span>
        <span class="contact__label">Fax</span><span class="contact__value">555-907-4418</span>
        <span class="contact__label">Email</span><span class="contact__value">tom@brantandcollc.example</span>
        <span class="contact__label">Web</span><span class="contact__value">brantandcollc.example</span>
      </div>
    </div>
  </section>

  <section class="card card--white card--back-white">
    <div class="brand brand--back"><span class="brand__mark"></span>Brant &amp; Co. LLC</div>
    <p class="web-line">brantandcollc.example</p>
  </section>

  <section class="card card--black card--back-black">
    <div class="brand brand--back"><span class="brand__mark"></span>Brant &amp; Co. LLC</div>
    <p class="web-line">brantandcollc.example</p>
  </section>

</main>
</body>
</html>
```